CoinVale Landing Page | A free, personalized stock market email

We are looking for someone to revamp our landing page at https://coinvale.example . You should get to know the product and what it offers, and present new designs for our landing page. Feel free to use assets that currently exist on the page, as well as any new assets that you can put together. This landing page should make it obvious what the product does and aim to dramatically increase our conversion rate. We are looking for creativity, uniqueness, and clarity of purpose.

Target Market(s)

People who are invested in, or interested in being invested in, the stock market

Industry/Entity Type

Finance

Number of Pages Required

1 page

Font styles to use
Sans Serif

Requirements
Must have
• Creativity, sleek/minimal design, existing color palette and logos
Nice to have
• Effective copy
Should not have
• Clutter

```html
<!DOCTYPE html>
<html lang="en">
<head>
<meta charset="utf-8">
<title>CoinVale — Do Less. Know More.</title>
<link rel="stylesheet" href="https://fonts.googleapis.com/css2?family=Figtree:wght@400;500;600;700;800&display=swap">
<style>
:root{
  --ink:#141a24;
  --muted:#4a5261;
  --light:#9aa3b0;
  --blue:#2a94d1;
  --blue-grad:linear-gradient(90deg,#1d8fd6,#2cb7e0);
  --navy:#2e5890;
  --green:#1db58a;
  --green-soft:#bfe6c8;
  --band:#f2f4f7;
  --line:#e3e6eb;
  --white:#fff;
}
*{box-sizing:border-box;margin:0;padding:0}
html,body{width:1200px;height:3788px;overflow:hidden}
body{position:relative;background:var(--white);font-family:'Figtree',sans-serif;color:var(--ink)}
.abs{position:absolute}
a{color:inherit;text-decoration:none}

/* nav */
.brand{font-weight:600;font-size:21px;color:var(--blue);display:flex;align-items:center;gap:7px}
.brand .dot{width:14px;height:14px;border-radius:50%;background:var(--blue)}
.nav-links{left:426px;top:27px;display:flex;gap:20px;font-size:11.5px;font-weight:600}
.btn{display:inline-flex;align-items:center;justify-content:center;border-radius:30px;background:var(--blue-grad);color:#fff;font-weight:600;box-shadow:0 6px 16px rgba(42,148,209,.3)}
.nav-btn{left:853px;top:15px;width:145px;height:42px;font-size:11.5px}

/* hero */
.eyebrow{font-size:10px;font-weight:600;color:var(--green)}
.display{font-weight:700;font-size:56px;line-height:59px;letter-spacing:-.5px}
.lead{font-size:11.5px;line-height:18px;color:var(--muted)}
.hero-cta{left:201px;top:456px;width:150px;height:51px;font-size:11.5px}
.sample-link{left:366px;top:474px;font-size:11.5px;font-weight:700;border-bottom:1.5px solid var(--ink);padding-bottom:2px}
.photo{background:radial-gradient(circle at 55% 40%,#c89878,#6b4a38 55%,#3d2b22)}

/* stock card */
.stock-card{background:#fff;border-radius:12px;box-shadow:0 10px 30px rgba(20,30,50,.12);padding:14px 12px;font-size:9px;color:var(--muted)}
.stock-card .tick{display:flex;align-items:center;gap:8px}
.stock-card .sym{font-size:15px;font-weight:700;color:var(--blue)}
.stock-card .price{background:#e8ecf1;border-radius:10px;padding:2px 8px;font-weight:700;color:var(--ink);font-size:11px}
.stock-card .co{margin-top:3px;font-size:8px}
.changes{display:flex;gap:14px;margin-top:9px}
.chg b{display:block;font-size:10px;color:var(--ink);font-weight:600}
.chg b::before{content:"";display:inline-block;margin-right:3px;border:4px solid transparent;vertical-align:1px}
.up b::before{border-bottom:5px solid var(--green);border-top:0}
.down b::before{border-top:5px solid #e0453a;border-bottom:0}
.chg span{font-size:7px;padding-left:10px}
.lbl{font-size:7.5px;letter-spacing:.5px;color:#c1c7d0;margin-top:12px;padding-top:8px;border-top:1px solid var(--line)}
.say{font-size:9.5px;color:var(--ink);margin-top:7px}
.rating{display:flex;align-items:center;gap:12px;margin-top:12px}
.buy{width:43px;height:40px;background:var(--green-soft);border-radius:3px;display:flex;align-items:center;justify-content:center;color:#6aa07a;font-weight:700;font-size:9px}
.bars{flex:1}
.bars i{display:block;height:4px;border-radius:2px;background:#e6e9ee;margin:4px 0}
.bars i:first-child{background:var(--green);width:86%}
.bars i:nth-child(2){width:50%}
.bars i:nth-child(3){width:20%}
.pcts{font-size:7.5px;line-height:10px;white-space:nowrap}
.target{display:flex;align-items:center;gap:8px;margin-top:12px}
.target .ring{width:16px;height:16px;border:2px solid var(--blue);border-radius:50%;position:relative}
.target .ring::after{content:"";position:absolute;inset:3px;background:var(--blue);border-radius:50%}
.target small{display:block;font-size:6.5px}
.target b{color:var(--ink);font-size:10px}
.ind{display:grid;grid-template-columns:1fr 1.6fr;font-size:8.5px;color:var(--ink);margin:8px 10px 0}
.ind span{padding:5px 0;border-bottom:1px solid var(--line)}
.ind .h{font-weight:600;border-bottom:1px solid #9aa3b0}
.news{display:flex;gap:8px;margin-top:8px;background:#f3f6f9;padding:6px;border-radius:4px}
.news .thumb{width:36px;height:36px;background:linear-gradient(135deg,#b7a391,#5d6b7a);flex:none}
.news b{font-weight:500;font-size:9px;color:var(--ink);line-height:11px;display:block}
.news small{font-size:6.5px;color:var(--light)}

/* section 2 */
.band{left:0;width:1200px;background:var(--band)}
.h2{font-weight:600;font-size:34px;line-height:40px}
.feature{width:237px;height:406px;border-radius:16px;color:#fff;padding:52px 34px 0}
.feature h3{font-size:22px;line-height:29px;font-weight:700}
.feature p{font-size:11px;line-height:19.5px;margin-top:14px;opacity:.92}
.feature .strong{font-weight:700;font-size:13px;opacity:1;margin-top:12px;line-height:16px}
.feature .art{position:absolute;left:78px;top:255px;width:80px;height:110px;border-radius:40px;background:rgba(255,255,255,.18)}
.f-blue{background:var(--blue)}
.f-navy{background:var(--navy)}
.f-green{background:var(--green)}

/* section 3 */
.center{left:0;width:1200px;text-align:center}
.h2c{font-weight:600;font-size:33px;line-height:40px}
.phone{width:178px;height:374px;border:5px solid var(--ink);border-radius:16px;background:#fff;overflow:hidden;padding:20px 14px;font-size:7px;color:var(--muted)}
.phone::before{content:"";position:absolute;left:50%;top:-1px;width:80px;height:10px;margin-left:-40px;background:var(--ink);border-radius:0 0 8px 8px}
.phone .pb{font-size:8px;color:var(--blue);text-align:center;font-weight:600;margin-bottom:10px}
.phone h4{font-size:10.5px;color:var(--ink);font-weight:700;margin:4px 0 6px}
.row{display:flex;justify-content:space-between;align-items:center;border-bottom:1px solid var(--line);padding:5px 0;font-size:6px;color:var(--ink)}
.tg{width:14px;height:7px;border-radius:4px;background:#d5d9df;position:relative}
.tg::after{content:"";position:absolute;top:1px;left:1px;width:5px;height:5px;border-radius:50%;background:#fff}
.tg.on{background:#5cc776}
.tg.on::after{left:8px}
.step h3{font-size:21px;font-weight:700}
.step p{font-size:11px;line-height:19.5px;color:var(--muted);margin-top:8px}

/* footer */
.foot-links{left:363px;top:3512px;font-size:13px;font-weight:600;line-height:25px}
.social{left:725px;top:3512px;font-size:13px;font-weight:600;line-height:25px}
.social li{list-style:none;display:flex;align-items:center;gap:7px}
.social li::before{content:"";width:9px;height:9px;border-radius:2px;background:var(--green)}
.copy{font-size:10px;color:var(--ink)}
</style>
</head>
<body>

<div class="abs" style="left:0;top:3300px;width:1200px;height:488px;background:radial-gradient(ellipse at 50% 100%,#d6eaf7 0%,#eef6fc 45%,#fff 80%)"></div>
<div class="abs" style="left:700px;top:0;width:500px;height:300px;background:radial-gradient(ellipse at 70% 30%,#eaf4fb,#fff 70%)"></div>

<header>
  <div class="abs brand" style="left:204px;top:22px"><span class="dot"></span>CoinVale</div>
  <nav class="abs nav-links"><a>Products</a><a>Insights</a><a>About</a><a>Pricing</a><a>Resources</a></nav>
  <a class="abs btn nav-btn">Sign up for FREE</a>
</header>

<section class="hero">
  <p class="abs eyebrow" style="left:204px;top:226px">Market Intelligence and Investment Analysis</p>
  <h1 class="abs display" style="left:202px;top:237px">Do Less.<br>Know More.</h1>
  <p class="abs lead" style="left:204px;top:373px;width:310px">Etiam ut erat sit amet neque sodales sodales sit amet non turpis. Nam scelerisque gravida nulla, sed tempor. Proin pulvinar dui in ante faucibus, in efficitur velit</p>
  <a class="abs btn hero-cta">Sign up for FREE</a>
  <a class="abs sample-link">See a Full Email Sample</a>

  <div class="abs photo" role="img" aria-label="Smiling young man checking stock insights on his phone" style="left:662px;top:140px;width:472px;height:475px;border-radius:0 50% 50% 50%"></div>

  <div class="abs stock-card" style="left:601px;top:176px;width:244px">
    <div class="tick"><span class="sym">QZVS</span><span class="price">$199.10</span></div>
    <p class="co">Solqira Energy, Inc.</p>
    <div class="changes"><div class="chg up"><b>+2.89%</b><span>1-Day</span></div><div class="chg down"><b>-3.89%</b><span>30-Day</span></div><div class="chg up"><b>+10.67%</b><span>1-Year</span></div></div>
    <p class="lbl">ANALYST RATINGS</p>
    <p class="say">What 35 market analysts are saying:</p>
    <div class="rating"><div class="buy">BUY</div><div class="bars"><i></i><i></i><i></i></div><div class="pcts">54.3% &nbsp;Buy<br>31.4% &nbsp;Hold<br>14.3% &nbsp;Sell</div></div>
    <div class="target"><span class="ring"></span><div><small>Target Price</small><b>$205</b></div></div>
    <p class="lbl">INDICATORS</p>
    <div class="ind"><span class="h">Signal</span><span class="h">Type</span><span>Drift Bands</span><span>BUY</span></div>
    <p class="lbl">NEWS</p>
    <div class="news"><div class="thumb" role="img" aria-label="Solar panels thumbnail"></div><div><b>Top 10 Solar Stocks To Watch This Year</b><small>By Dana Reel via Ledgerleaf Daily</small></div></div>
  </div>

  <div class="abs" style="left:820px;top:557px;width:244px;height:69px;background:var(--green);border-radius:8px;box-shadow:0 10px 24px rgba(29,181,138,.3);color:#fff;padding:14px 16px;font-size:10px;font-weight:600;line-height:14px">
    Last 7 days<br>▲ +22,12
    <svg class="abs" style="left:70px;top:10px" width="160" height="50" viewBox="0 0 160 50"><polyline points="0,40 15,28 30,34 45,24 60,38 75,30 90,36 105,22 120,14 135,6 160,42" fill="none" stroke="#fff" stroke-width="2"/><circle cx="135" cy="6" r="4" fill="#2e5890"/></svg>
  </div>
</section>

<section>
  <div class="abs band" style="top:757px;height:431px"></div>
  <h2 class="abs h2" style="left:220px;top:856px">CoinVale is your<br>free, personalized,<br>data-driven<br>finance email</h2>
  <p class="abs lead" style="left:220px;top:1032px;width:310px">Mauris nunc ligula, laoreet nec odio eget, posuere porta quam. Nam efficitur vulputate nunc eu facilisis.</p>
  <div class="abs" role="img" aria-label="Smiling woman looking at her phone" style="left:650px;top:750px;width:340px;height:438px;border-radius:170px 170px 0 0;background:linear-gradient(180deg,#8a5a44 0%,#d6a58a 35%,#5c5a58 70%,#4a4846)"></div>
  <div class="abs" style="left:948px;top:831px;width:111px;height:110px;background:#fff;border-radius:8px;box-shadow:0 8px 20px rgba(20,30,50,.12);padding:8px 8px">
    <div style="font-size:9px;font-weight:600">2201</div>
    <div style="font-size:7.5px;color:var(--green)">▲ +22,12</div>
    <svg width="95" height="70" viewBox="0 0 95 70"><defs><linearGradient id="ag" x1="0" y1="0" x2="0" y2="1"><stop offset="0" stop-color="#2a94d1"/><stop offset="1" stop-color="#2e5890"/></linearGradient></defs><path d="M0,70 L0,50 8,38 15,52 22,30 30,48 38,22 46,46 54,18 60,44 68,10 76,38 84,28 95,50 95,70Z" fill="url(#ag)"/></svg>
  </div>

  <article class="abs feature f-blue" style="left:219px;top:1145px"><h3>Stop scanning charts and chasing data</h3><p>Don't bend over backwards to get the investment insights you need. You have better ways to spend your time and energy.</p><div class="art" role="img" aria-label="Magnifying glass illustration"></div></article>
  <article class="abs feature f-navy" style="left:481px;top:1145px"><h3>Let the information come to you</h3><p>We'll send you curated market-ing insights exactly when you want them.</p><div class="art" role="img" aria-label="Rocket illustration"></div></article>
  <article class="abs feature f-green" style="left:744px;top:1145px"><h3>Stop paying for information</h3><p class="strong">CoinVale is free. Period.</p><p style="margin-top:10px">Don't spend a dime on financial information, use that money for investments</p><div class="art" role="img" aria-label="Gift bow illustration"></div></article>
</section>

<section>
  <div class="abs band" style="top:2040px;height:430px"></div>
  <p class="abs center eyebrow" style="top:1709px">Investment Analysis Straight to You</p>
  <h2 class="abs center h2c" style="top:1723px">Curated insights exactly<br>when you want them.</h2>

  <div class="abs phone" style="left:257px;top:1838px">
    <p class="pb">‹ &nbsp; CoinVale</p>
    <h4>Your Schedule</h4>
    <p>Currently, we only offer send times during NXSE trading hours.</p>
    <p style="margin:4px 0 8px">Your timezone is: America/New_York</p>
    <div class="row"><span>9:30 AM</span><i class="tg on"></i></div>
    <div class="row"><span>10:00 AM</span><i class="tg"></i></div>
    <div class="row"><span>10:30 AM</span><i class="tg on"></i></div>
    <div class="row"><span>11:00 AM</span><i class="tg"></i></div>
    <div class="row"><span>11:30 AM</span><i class="tg"></i></div>
    <div class="row"><span>12:00 PM</span><i class="tg"></i></div>
    <div class="row"><span>12:30 PM</span><i class="tg on"></i></div>
    <div class="row"><span>1:00 PM</span><i class="tg"></i></div>
    <div class="row"><span>1:30 PM</span><i class="tg"></i></div>
  </div>

  <div class="abs phone" style="left:509px;top:1838px">
    <p class="pb">‹ &nbsp; CoinVale</p>
    <h4>Voltqix Corporation (XQVT)</h4>
    <div class="row" style="border:0"><span>Toggle All</span><i class="tg on"></i></div>
    <p style="margin-top:18px">Data</p>
    <div class="row"><span>Price</span><i class="tg on"></i></div>
    <div class="row"><span>News</span><i class="tg on"></i></div>
    <div class="row"><span>Analyst Ratings</span><i class="tg on"></i></div>
    <p style="margin-top:12px">Indicators</p>
    <div class="row"><span>Drift Bands</span><i class="tg on"></i></div>
    <div class="row"><span>MACD</span><i class="tg on"></i></div>
    <div class="row"><span>Relative Strength Index</span><i class="tg on"></i></div>
  </div>

  <div class="abs phone" style="left:764px;top:1838px">
    <p class="pb" style="font-size:13px">CoinVale</p>
    <p style="text-align:center;margin-bottom:10px">4:30 PM, June 30 2023</p>
    <p style="color:var(--blue);font-weight:700;font-size:8px">XQVT <span style="color:var(--ink)">$393.27</span></p>
    <p>Voltqix Corporation</p>
    <p style="margin-top:6px">+6.11% &nbsp; +35.41% &nbsp; +108.82%</p>
    <p style="margin-top:8px">What 41 market analysts are saying:</p>
    <div style="display:flex;gap:8px;margin-top:6px;align-items:center"><div class="buy" style="width:26px;height:24px;font-size:6px">BUY</div><div class="bars" style="flex:1"><i></i><i></i></div><span>85.4%</span></div>
    <div class="row" style="margin-top:12px"><span>Drift Bands</span><span>BUY</span></div>
    <div class="news" style="margin-top:12px"><div class="thumb" style="width:22px;height:22px" role="img" aria-label="News thumbnail"></div><b style="font-size:6px;line-height:8px">Ria Holt on Voltqix, AI investments and new strategy</b></div>
    <p style="color:var(--blue);font-weight:700;font-size:8px;margin-top:14px">ZQRB <span style="color:var(--ink)">$140.47</span></p>
  </div>

  <div class="abs step" style="left:262px;top:2255px;width:180px"><h3>Your Schedule</h3><p>Customize when you get your email. Up to every half an hour during NXSE trading hours.</p></div>
  <div class="abs step" style="left:516px;top:2255px;width:180px"><h3>Your Assets</h3><p>Choose from thousands of assets to include inyour email. QKXY, ZQRB, WQZV and more!</p></div>
  <div class="abs step" style="left:776px;top:2255px;width:170px"><h3>All the Data</h3><p>We provide as much data on assets as we can,including price, price change, analyst ratings, technical indicators, and news.</p></div>
</section>

<section>
  <p class="abs center eyebrow" style="top:2653px">Get Started with CoinVale Meta</p>
  <h2 class="abs center display" style="top:2664px">Do Less.<br>Know More Today.</h2>
  <div class="abs photo" role="img" aria-label="Two friends laughing while looking at a phone in front of a brick wall" style="left:262px;top:2830px;width:605px;height:478px;border-radius:240px 240px 0 240px;background:linear-gradient(120deg,#9a5a44,#6b4a3a 50%,#3b3a3a)"></div>
  <div class="abs stock-card" style="left:603px;top:2852px;width:264px">
    <div class="tick"><span class="sym">QZVS</span><span class="price">$199.10</span></div>
    <p class="co">Solqira Energy, Inc.</p>
    <div class="changes"><div class="chg up"><b>+2.89%</b><span>1-Day</span></div><div class="chg down"><b>-3.89%</b><span>30-Day</span></div><div class="chg up"><b>+10.67%</b><span>1-Year</span></div></div>
    <p class="lbl">ANALYST RATINGS</p>
    <p class="say">What 35 market analysts are saying:</p>
    <div class="rating"><div class="buy">BUY</div><div class="bars"><i></i><i></i><i></i></div><div class="pcts">54.3% &nbsp;Buy<br>31.4% &nbsp;Hold<br>14.3% &nbsp;Sell</div></div>
    <div class="target"><span class="ring"></span><div><small>Target Price</small><b>$205</b></div></div>
    <p class="lbl">INDICATORS</p>
    <div class="ind"><span class="h">Signal</span><span class="h">Type</span><span>Drift Bands</span><span>BUY</span></div>
    <p class="lbl">NEWS</p>
    <div class="news"><div class="thumb" role="img" aria-label="Solar panels thumbnail"></div><div><b>Top 10 Solar Stocks To Watch This Year</b><small>By Dana Reel via Ledgerleaf Daily</small></div></div>
  </div>
  <div class="abs" role="img" aria-label="Two women smiling at a phone" style="left:857px;top:3175px;width:118px;height:118px;border-radius:50%;background:radial-gradient(circle,#e9d2c2,#c79a82 60%,#a8b0a8)"></div>
</section>

<footer>
  <ul class="abs foot-links" style="list-style:none"><li>About</li><li>Blog</li><li>Terms of Use</li><li>Privacy Policy</li></ul>
  <div class="abs" style="left:540px;top:3520px;width:120px;text-align:center;font-size:24px;font-weight:700;color:var(--blue);line-height:80px">CoinVale</div>
  <ul class="abs social"><li>Clipwave</li><li>Streamora</li></ul>
  <div class="abs brand" style="left:540px;top:3685px;width:120px;justify-content:center"><span class="dot"></span>CoinVale</div>
  <p class="abs center copy" style="top:3729px">Copyright © 2023 CoinVale LLC</p>
</footer>

</body>
</html>
```